Gestaltung eines Merkblattes
Ein Entwurf, der genau meinen Vorstellungen entspricht. Eine Abwicklung, die schneller und professioneller nicht sein könnte. Die Kommunikation - sehr symphatisch und kundenorientiert. Resumee: Besser geht es nicht.
Zielgruppe
www.hufspur-praxis.de/ Medizinische Bioresonanzanalysen für Pferde. Die Kundschaft besteht hauptsächlich aus Frauen, Alter von 20- 55 Jahre.
Bei dem Projekt handelt es sich um die Gestaltung eines wichtigen Merkblattes, das jedem Kunde zusammen mit dem Befund der Analyse gemailt wird. Es enthält wichtige Informationen rund um die Bioresonanzanalyse und sollte als pdf- Datei vorliegen.
Aufgabenstellung
Kernproblem: Die Kunden lesen das Merkblatt gar nicht oder nicht sorgfältig. So entstehen viele Fragen in der Folge, die nicht notwendig wären.
Wir benötigen eine pdf- Datei, die zum Lesen anregt, gerne gelesen wird und in der die wichtigsten Aspekte in das Auge fallen. Diese wurden von mir in der Worddatei, die den Text enthält, rot markiert.
Der Text in schwarz ist deutlich weniger wichtig.
Ach ja, die Überschrift ist doof. 'Allgemeine Hinweise' das animiert nicht wirklich zum Lesen. Falls Sie eine griffige Idee haben, sehr gerne.

```html
<!DOCTYPE html>
<html lang="de">
<head>
<meta charset="utf-8">
<title>Leitfaden zur Handhabung – Hufspur-Praxis</title>
<link href="https://fonts.googleapis.com/css2?family=Cinzel:wght@600;700&family=Quicksand:wght@400;600&display=swap" rel="stylesheet">
<style>
  :root{
    --green-dark:#8aa62c;
    --green-mid:#97b03e;
    --green-light:#a8bd62;
    --green-text:#8ca530;
    --paper:#ffffff;
    --backdrop:#e8e5e1;
  }
  *{box-sizing:border-box;margin:0;padding:0}
  html,body{width:1016px;height:1200px;overflow:hidden;background:var(--backdrop)}
  body{font-family:'Quicksand',sans-serif;position:relative}
  .sheet{position:absolute;top:250px;width:472px;height:668px;background:var(--paper);overflow:hidden;box-shadow:0 6px 18px rgba(0,0,0,.18)}
  .sheet--front{left:24px}
  .sheet--back{left:520px}

  .ticker{position:absolute;top:0;left:0;right:0;height:15px;background:var(--green-dark);color:#fff;font-family:'Cinzel',serif;font-size:7.4px;font-weight:600;letter-spacing:.3px;line-height:15px;white-space:nowrap;overflow:hidden;text-align:center;z-index:3}

  .hero-photo{position:absolute;top:15px;right:0;width:56%;height:300px;background:linear-gradient(180deg,#ecebe2 0%,#d9cdb3 35%,#a2714b 62%,#7b9248 100%)}
  .hero-swoosh{position:absolute;top:15px;left:0;width:100%;height:300px;z-index:1}
  .brand{position:absolute;z-index:2;display:flex;align-items:center;gap:5px;font-family:'Quicksand',sans-serif;font-weight:600;color:var(--green-text);font-size:11px}
  .brand::before{content:"";width:9px;height:9px;border-radius:50%;background:var(--green-text)}
  .sheet--front .brand{top:70px;left:72px}
  .title{position:absolute;z-index:2;top:132px;left:24px;width:196px;text-align:center;font-family:'Cinzel',serif;font-weight:700;color:var(--green-text);font-size:18px;line-height:23px}
  .title::after{content:"";display:block;margin:6px auto 0;width:140px;border-bottom:1px dotted var(--green-text)}

  .col{position:absolute;color:#fff;padding:20px 18px}
  .col h2{font-family:'Cinzel',serif;font-weight:700;font-size:10.5px;letter-spacing:.4px;line-height:13px;margin-bottom:7px}
  .col h2::after{content:"";display:block;margin-top:4px;width:70%;border-bottom:1px dotted rgba(255,255,255,.8)}
  .col p{font-size:6.9px;line-height:9.6px;margin-bottom:8px;text-align:justify;hyphens:auto}
  .col p.key{font-weight:600}
  .col section+section{margin-top:8px}

  .sheet--front .col--left{top:315px;left:0;width:50%;height:353px;background:var(--green-dark)}
  .sheet--front .col--right{top:315px;left:50%;width:50%;height:353px;background:var(--green-light)}

  .sheet--back .col--left{top:0;left:0;width:50%;height:530px;background:var(--green-dark)}
  .back-photo{position:absolute;top:0;right:0;width:50%;height:330px;background:linear-gradient(160deg,#c7ccd6 0%,#e9e3d8 40%,#a68d66 70%,#6f6049 100%)}
  .sheet--back .brand{top:40px;right:16px}
  .sheet--back .col--doping{top:330px;right:0;width:50%;height:338px;background:var(--green-light)}
  .contact{position:absolute;left:0;bottom:0;width:50%;height:138px;background:var(--paper);padding:18px 18px;color:var(--green-text)}
  .contact h2{font-family:'Cinzel',serif;font-weight:700;font-size:12px;margin-bottom:8px}
  .contact p{font-size:7.2px;line-height:10.5px;margin-bottom:5px}
  .contact strong{font-weight:600}
  .contact .phone-line{display:flex;align-items:center;gap:4px}
</style>
</head>
<body>

<article class="sheet sheet--front">
  <div class="ticker">+ BITTE SORGFÄLTIG LESEN +++ BITTE SORGFÄLTIG LESEN +++ BITTE SORGFÄLTIG LESEN ++</div>
  <div class="hero-photo" role="img" aria-label="Foto: Pony mit heller Mähne auf einer Weide"></div>
  <svg class="hero-swoosh" viewBox="0 0 472 300" preserveAspectRatio="none" aria-hidden="true">
    <path d="M0 0 H275 C250 90 225 200 215 300 H0 Z" fill="#fbfaf6"/>
    <path d="M275 0 C250 90 225 200 215 300" fill="none" stroke="#ffffff" stroke-opacity=".7" stroke-width="6"/>
    <path d="M0 250 H221 L215 300 H0 Z" fill="#9aa46a" opacity=".35"/>
  </svg>
  <div class="brand">Hufspur-Praxis</div>
  <h1 class="title">Leitfaden zur Handhabung</h1>

  <div class="col col--left">
    <section>
      <h2>Das Wichtigste zuerst</h2>
      <p>Die empfohlenen Präparate können (wenn nicht anders angegeben) in das normale Kraftfutter gegeben werden. Tropfen und Bachblüten bitte auf ein kleines Stück trockenes Brot, Zwieback, bei Pferden, die kein Getreide fressen dürfen, auf ein Stück Reiswaffel geben, und dem Pferd direkt füttern.</p>
      <p>Mineralis Pulver muss nicht, wie vom Hersteller angegeben, in Wasser aufgelöst werden. Eine Gabe in das Kraftfutter, Heucobs etc. vermindert nicht die Wirkung.</p>
      <p>Bitte füttern Sie alle Präparate, außer es sind abweichende Empfehlungen vorhanden, ohne Unterbrechung, bis Ihnen das Ergebnis der ersten Nachtestung vorliegt. Pausen von mehr als zwei Tagen können zu Beginn der Behandlung die positive Entwicklung Ihres Pferdes beeinträchtigen.</p>
      <p>Falls Ihr Pferd sehr wählerisch ist bei der Zufütterung von Präparaten in Pellets- oder Pulverform, dann beginnen Sie mit einer sehr kleinen Dosierung von z. B. ½ Teelöffel und steigern diese sehr langsam. Bei trockenem Futter (Müsli, Hafer) sortieren manche Pferde gerne aus. Hier ist es sinnvoll, das Futter anzufeuchten, etwas Heucobs oder getreidefreies Mash dazuzugeben.</p>
    </section>
  </div>

  <div class="col col--right">
    <section>
      <h2>Nachtestung</h2>
      <p>Wir bestätigen den Eingang der Probe zur Nachtestung nicht. In regelmäßigen Abständen werden alle Befunde nachgetestet. Wir senden Ihnen im Anschluss per Mail das neue Ergebnis mit einer aktualisierten Therapieempfehlung zu.</p>
      <p class="key">Wir brauchen für die Nachtestung eine neue Haarprobe und ein kurzes Feedback zu der aktuellen Entwicklung Ihres Pferdes. Mehr nicht.</p>
    </section>
    <section>
      <h2>Bachblüten</h2>
      <p>Wenn die Therapieempfehlung eine Übersicht an Bachblüten enthält, dann spiegeln diese den seelischen Zustand Ihres Pferdes wieder, der von seinen aktuellen Lebensbedingungen, seiner körperlichen Belastung durch Krankheit und durch Abläufe in seiner Herde beeinflusst wird. Erfahrungsgemäß bezieht sich die Darstellung der Blüten bei Pferden, die in einer Herde leben, häufig mehr auf die Gefühle des Pferdes gegenüber seinen Artgenossen als auf den Kontakt mit dem Menschen.</p>
      <p>Die meisten Apotheken kennen sich aus mit der Herstellung einer Bachblütenmischung. Falls nicht, hier die Anleitung: in ein 30 ml Medizinfläschchen mit Tropfvorrichtung oder Pipette gibt man 10 ml Alkohol (Brandy oder Weinbrand), 20 ml Quellwasser oder stilles Mineralwasser (ohne Kohlensäure; kein destilliertes Wasser!) und 2-3 Tropfen von jeder Blüte, die im Moment benötigt wird. Als Alternative zu Alkohol kann auch Obstessig eingesetzt werden.</p>
    </section>
  </div>
</article>

<article class="sheet sheet--back">
  <div class="col col--left">
    <section>
      <h2>Tierarzt</h2>
      <p class="key">Wir weisen ausdrücklich darauf hin, dass die Ergebnisse der Bioresonanzanalyse nicht kompatibel mit den herkömmlichen Labormethoden und tierärztlichen Diagnoseformen sind.</p>
      <p>Wenn wir eine Belastung der Leber mit Bioresonanz feststellen, kann ein Blutbild beim Tierarzt zu dem gleichen Zeitpunkt unauffällig sein. Der Grund hierfür liegt in der unterschiedlichen Beurteilung.</p>
      <p>Bekommt Ihr Pferd Medikamente, relevant sind Antibiotika oder massiv entzündungshemmende Mittel, dann sprechen wir mit Ihnen ab, ob die Nachtestung verschoben wird. Impfungen sind für die Durchführung der Nachtestung nicht von Bedeutung.</p>
    </section>
    <section>
      <h2>Impfung</h2>
      <p>Wir geben generell keine Impfempfehlungen. Es hat sich jedoch in den vergangenen Jahren gezeigt, dass es sinnvoll ist, Impfungen (besonders Influenza- und Herpes- Impfungen) vor Beginn der Umsetzung der Therapieempfehlung einzuplanen. Werden sie zu einem späteren Zeitpunkt vorgenommen, kann es zu Rückschritten in der ansonsten positiven Entwicklung kommen.</p>
    </section>
    <section>
      <h2>Tragende Stuten/ Stuten mit Fohlen bei Fuß</h2>
      <p>Wir übernehmen keine Haftung für die Gabe der von uns empfohlenen Naturheilmittel bei tragenden Stuten und Stuten mit Fohlen bei Fuß. Jedes der angegebenen Mittel wurde von mir mit großer Sorgfalt ausgewählt. Die aktuell vorhandenen, medizinischen Studien zu der Wirkung von Naturheilmitteln bei tragenden Stuten sind jedoch nicht umfangreich genug, um Nebenwirkungen vollständig ausschließen zu können.</p>
    </section>
  </div>

  <div class="back-photo" role="img" aria-label="Foto: helles Pferd mit grauer Mähne vor weiter Landschaft"></div>
  <div class="brand">Hufspur-Praxis</div>

  <div class="col col--doping">
    <section>
      <h2>Doping</h2>
      <p>Zum Schutz der Pferde bestehen Anti- Doping Richtlinien, die klare Regeln vorgeben, welche Zu- satzfutterpräparate, Medikamente und auch Naturheilmittel einem Turnierpferd vor und während einem Start in einer Turnierprüfung gefüttert werden dürfen. Die Einhaltung der Vorgaben wird durch stichpunktartige Kontrollen überprüft.</p>
      <p>Bitte beachten Sie die Anti- Doping Richtlinien der Reitverband und weiterer Pferdesportverbände und halten Sie bei der Fütterung aller Präparate unserer Therapieempfehlung eine Karenzzeit von 48 Stunden vor Prüfungsbeginn ein, wenn Sie mit Ihrem Pferd an einem Wettbewerb teilnehmen. Ausnahme! Bei der Zufütterung von Präparaten, die Teufelskralle enthalten, besteht eine Karenzzeit von 4 Tagen.</p>
      <p>Wir übernehmen für die Folgen einer Nichtbeachtung der nationalen oder internationalen Anti-Dopingrichtlinien keine Haftung.</p>
    </section>
  </div>

  <div class="contact">
    <h2>Gibt es noch Fragen?</h2>
    <p>Melden Sie sich gerne bei mir:</p>
    <p class="phone-line">
      <svg width="8" height="8" viewBox="0 0 24 24" aria-hidden="true"><path fill="#8ca530" d="M6.6 10.8a15 15 0 0 0 6.6 6.6l2.2-2.2a1 1 0 0 1 1-.25 11.4 11.4 0 0 0 3.6.57 1 1 0 0 1 1 1V20a1 1 0 0 1-1 1A17 17 0 0 1 3 4a1 1 0 0 1 1-1h3.5a1 1 0 0 1 1 1c0 1.25.2 2.45.57 3.570a1 1 0 0 1-.25 1z"/></svg>
      <strong>Tel. 06541-2290</strong>
    </p>
    <p>Sie erreichen mich telefonisch Montag- Donnerstag in der Zeit von 17:00- 18:00 Uhr und während der klassischen Bürozeiten per Email unter <strong>info@hufspur-praxis.net</strong></p>
  </div>
</article>

</body>
</html>
```